College presentation for a startup bootcamp - how to talk to customers

I need a simple design for a college PowerPoint/ search slide presentation for students that are going through a Startup BootCamp. No flashy colors
- Accessible font - or provide the font - I like the vorel's website font or normal text font
- use a neutral colors schemes of grays - with 1-2 highlight colors
- You can use the photos in the presentation or others
- Urgent the presentation is on Thursday - I will award the winner on Wednesday.
- It's 23 slides long.

Target Market(s)

College students interested in startups

Industry/Entity Type

College

Font styles to use
Serif
Sans Serif
Other font styles liked:
• helvetica

Colors

Designer to choose only greyscale colors for use in the design.

Requirements
Must have
• clean , simple design neural colors like greyscale with 1-3 pop colors
Should not have
• no flashy colors, or hard to read text

```html
<!DOCTYPE html>
<html lang="en">
<head>
<meta charset="utf-8">
<title>Customer Development – Mom's Test</title>
<link href="https://fonts.googleapis.com/css2?family=Outfit:wght@300;400;500;600;700&display=swap" rel="stylesheet">
<style>
:root{
  --stage:#4a4748;
  --paper:#efefef;
  --soft:#e2e2e2;
  --mid:#8e8e8e;
  --steel:#6a6a6a;
  --dark:#3e3e3e;
  --ink:#1f1f1f;
  --accent:#6b63f6;
  --alert:#e0262a;
  --photo:linear-gradient(135deg,#cfcfcf,#8d8d8d 60%,#5c5c5c);
  --photo-dark:linear-gradient(135deg,#6d6d6d,#2e2e2e);
}
*{box-sizing:border-box;margin:0;padding:0}
html,body{width:1200px;height:1075px;overflow:hidden;background:var(--stage)}
body{font-family:"Outfit",Helvetica,Arial,sans-serif;color:var(--ink)}
.deck{position:absolute;left:40px;top:42px;display:grid;grid-template-columns:repeat(4,270px);grid-auto-rows:152px;column-gap:13.5px;row-gap:16.2px}
.slide{position:relative;background:var(--paper);overflow:hidden}
.page{position:absolute;right:6px;bottom:4px;font-size:4px;color:var(--mid)}
.photo{position:absolute;background:var(--photo)}
.photo.dark{background:var(--photo-dark)}
.title{position:absolute;left:0;right:0;text-align:center;font-weight:600;font-size:10.5px;line-height:1.1}
.hl{color:var(--accent)}
ul{list-style:none}
li{position:relative;padding-left:5px;margin-bottom:1.6px}
li::before{content:"•";position:absolute;left:0}
li.sub{padding-left:10px}
li.sub::before{content:"–";left:4px}
.band{position:absolute;left:0;right:14px;top:41px;height:91px;display:flex}
.good{flex:1;background:var(--soft);padding:6px 8px;font-size:5px;line-height:1.2}
.bad{flex:1;background:var(--mid);color:#fff;padding:6px 8px;font-size:5px;line-height:1.2}
.tag{font-size:6.5px;display:flex;align-items:center;gap:3px;margin-bottom:5px}
.tag svg{width:12px;height:12px}
.card{position:absolute;left:81px;top:15px;width:173px;height:121px;background:#fff;padding:12px 12px}
.card .kick{font-size:8px;color:var(--steel);font-weight:500}
.card h3{font-size:10.5px;font-weight:600;margin-bottom:6px}
.card ul{font-size:4.9px;line-height:1.25}
.step{font-size:9.5px;color:var(--accent);font-weight:600}
.people-copy{position:absolute;left:14px;width:102px;top:48px;text-align:right;font-size:5.4px;line-height:1.65;z-index:1}
</style>
</head>
<body>
<main class="deck">

<section class="slide">
  <div class="photo" style="inset:0;background:linear-gradient(120deg,#e8e8e8,#9a9a9a 55%,#555)" role="img" aria-label="Black and white photo of students working together at a table"></div>
  <div style="position:absolute;left:17px;top:38px;width:149px;height:76px;background:rgba(107,99,246,.85);padding:12px 13px;color:#fff">
    <h1 style="font-size:15px;font-weight:600;line-height:1">CUSTOMER<br>DEVELOPMENT</h1>
    <p style="font-size:5.5px;margin-top:5px;font-weight:300">Mom's Test - How to Talk To Customers</p>
  </div>
</section>

<section class="slide">
  <div style="position:absolute;left:0;top:0;bottom:0;width:95px;background:#e4e4e4"></div>
  <p style="position:absolute;left:15px;top:32px;font-size:8px;color:var(--steel);line-height:1">Mom's test<br><b style="font-size:11px;font-weight:600">Agenda</b></p>
  <div style="position:absolute;left:68px;top:30px;width:190px;font-size:16px;font-weight:600;color:var(--steel);line-height:1">
    <div style="display:flex;gap:8px;height:24px"><span>01</span><span style="font-size:4.5px;color:var(--ink)"><b>WHAT IS THE PROBLEM?</b><br><span style="font-weight:300;font-size:3.5px">Here you could describe the topic of the section</span></span></div>
    <div style="display:flex;gap:8px;height:25px"><span>02</span><span style="font-size:4.5px;color:var(--ink)"><b>HOW TO TALK TO CUSTOMERS?</b><br><span style="font-weight:300;font-size:3.5px">Here you could describe the topic of the section</span></span></div>
    <div style="display:flex;gap:8px;height:24px"><span>03</span><span style="font-size:4.5px;color:var(--ink)"><b>HOW TO ASK QUESTIONS?</b><br><span style="font-weight:300;font-size:3.5px">Here you could describe the topic of the section</span></span></div>
    <div style="display:flex;gap:8px"><span>04</span><span style="font-size:4.5px;color:var(--ink)"><b>WHO TO TALK TO?</b><br><span style="font-weight:300;font-size:3.5px">Here you could describe the topic of the section</span></span></div>
  </div>
</section>

<section class="slide">
  <h2 class="title" style="top:14px">Customer development</h2>
  <svg viewBox="0 0 270 152" style="position:absolute;inset:0" font-family="Outfit,sans-serif">
    <g fill="none" stroke="var(--accent)" stroke-width="0.8">
      <rect x="13" y="36" width="57" height="98" rx="28"/>
      <rect x="75" y="36" width="57" height="98" rx="28"/>
      <rect x="138" y="36" width="57" height="98" rx="28"/>
      <rect x="200" y="36" width="57" height="98" rx="28"/>
      <path d="M52 132 Q70 144 88 134"/>
    </g>
    <g fill="#e6e6e6" stroke="#aaa" stroke-width="0.5">
      <rect x="22" y="66" width="39" height="14" rx="7"/><rect x="22" y="86" width="39" height="14" rx="7"/><rect x="22" y="106" width="39" height="14" rx="7"/>
      <rect x="84" y="66" width="39" height="14" rx="7"/><rect x="84" y="86" width="39" height="14" rx="7"/><rect x="84" y="106" width="39" height="16" rx="8"/>
      <rect x="147" y="66" width="39" height="50" rx="19"/>
      <rect x="209" y="66" width="39" height="24" rx="12"/><rect x="209" y="96" width="39" height="16" rx="8"/>
    </g>
    <g font-size="6" fill="#222" text-anchor="middle">
      <text x="41.5" y="50">Customer</text><text x="41.5" y="58">Discovery</text>
      <text x="103.5" y="50">Customer</text><text x="103.5" y="58">Validation</text>
      <text x="166.5" y="50">Customer</text><text x="166.5" y="58">Creation</text>
      <text x="228.5" y="50">Company</text><text x="228.5" y="58">Building</text>
      <text x="72" y="129" font-size="5">Pivot</text>
    </g>
    <g font-size="3.2" fill="#333" text-anchor="middle">
      <text x="41.5" y="72">Problem-Solution</text><text x="41.5" y="76">Fit</text>
      <text x="41.5" y="94">Proposed MVP</text><text x="41.5" y="114">Proposed Funnels</text>
      <text x="103.5" y="72">Product-Market</text><text x="103.5" y="76">Fit</text>
      <text x="103.5" y="94">Business Model</text><text x="103.5" y="111">Sales and</text><text x="103.5" y="115">Marketing</text><text x="103.5" y="119">Roadmap</text>
      <text x="166.5" y="92">Scale Execution</text>
      <text x="228.5" y="77">Scale</text><text x="228.5" y="81">Organisation</text>
      <text x="228.5" y="105">Scale Operations</text>
    </g>
    <text x="250" y="144" font-size="2.6" text-anchor="end" fill="#444">Sam Harlow's Customer Development by Ben Corder, custlab.example</text>
  </svg>
  <span class="page">3</span>
</section>

<section class="slide">
  <div style="position:absolute;left:0;top:47px;width:11px;height:41px;background:#cfcfcf"></div>
  <div class="photo" style="left:126px;top:0;width:130px;height:152px" role="img" aria-label="Photo of two people hugging"></div>
  <div class="people-copy">
    <h3 style="font-size:11.5px;font-weight:600;margin-bottom:5px">People</h3>
    <p>People try to be <span class="hl">nice</span></p>
    <p>Therefore they lie in your face <span class="hl">without<br>realizing</span> it</p>
    <p style="color:var(--alert)">Bad data it worse than no data</p>
    <p>E.g. "I'll definitely buy that"</p>
    <p>THE PROBLEM</p>
  </div>
  <span class="page">4</span>
</section>

<section class="slide">
  <div class="photo" style="inset:0" role="img" aria-label="Photo of a smiling man in a suit pointing forward"></div>
  <div class="card">
    <p class="kick">Mom's test</p>
    <h3>What People <span class="hl">Say</span></h3>
    <ul style="font-size:5.2px;line-height:1.35">
      <li>You: Mom, I have a business idea. Do you have 5 mins?</li>
      <li>Mom: Of course, dear</li>
      <li>You: You life your tablet and use it a lot?</li>
      <li>Mom: Sure it's great.</li>
      <li>You: Would you buy a cookbook app?</li>
      <li>Mom: I love cookbooks, sounds nice. Does it come with vegan recipes? Or something special for Xmas?</li>
    </ul>
  </div>
  <span class="page">5</span>
</section>

<section class="slide">
  <div class="photo" style="inset:0" role="img" aria-label="Photo of a thoughtful man with glasses"></div>
  <div class="card">
    <p class="kick">Mom's test</p>
    <h3>What People <span class="hl">Think</span></h3>
    <ul style="font-size:3.8px;line-height:1.3">
      <li>You: Mom, I have a business idea. Do you have 5 mins?</li>
      <li>Mom: Of course, dear</li>
      <li class="sub">I'm proud of you and I don't want to hurt your feelings</li>
      <li>You: You life your tablet and use it a lot?</li>
      <li>Mom: Sure it's great.</li>
      <li class="sub">I use it to check email on the sofa</li>
      <li>You: Would you buy a cookbook app?</li>
      <li>Mom: I love cookbooks, sounds nice. Does it come with vegan recipes? Or something special for Xmas?</li>
      <li class="sub">Well, I have plenty of cookbooks. I don't need a computer in my kitchen - it might get dirty! But hey, if my kid made it, I'll try it. App? I never bought an app. Don't you need to enter your card for that? Let me try to change the subject.</li>
    </ul>
  </div>
  <span class="page">6</span>
</section>

<section class="slide">
  <div class="photo" style="inset:0" role="img" aria-label="Photo of a smiling woman giving a thumbs up"></div>
  <div class="card">
    <p class="kick">Mom's test</p>
    <h3 style="margin-bottom:3px">How to do it <span class="hl">Right</span></h3>
    <p style="font-size:7px;margin-bottom:3px">You:</p>
    <ul style="font-size:4.9px;line-height:1.35">
      <li>Mom, when have you last time used the tablet?</li>
      <li>For what?</li>
      <li>Have you ever used it in the kitchen?</li>
      <li>Have you ever bought an app? Which? Why? For how much?</li>
      <li>Do you use your cookbooks</li>
      <li>Is there anything you dislike about them?</li>
      <li>What was the last cookbook you bought? When? Why?</li>
    </ul>
  </div>
  <span class="page">7</span>
</section>

<section class="slide">
  <h2 class="title" style="top:15px">General <span class="hl">Rule of Thumb</span> to watch for</h2>
  <div class="photo" style="left:0;top:58px;width:80px;height:70px;background:linear-gradient(90deg,#f0f0f0,#b9b9b9)" role="img" aria-label="Photo of a hand giving a thumbs up"></div>
  <svg viewBox="0 0 270 152" style="position:absolute;inset:0" font-family="Outfit,sans-serif">
    <circle cx="107" cy="85" r="31" fill="var(--dark)"/>
    <circle cx="167" cy="85" r="31" fill="var(--accent)"/>
    <circle cx="227" cy="85" r="31" fill="var(--mid)"/>
    <g font-size="5.4" fill="#fff" text-anchor="middle">
      <text x="107" y="84">High frequency</text><text x="107" y="92">of usage</text>
      <text x="167" y="84">It is urgent/</text><text x="167" y="92">painful enough</text>
      <text x="227" y="84">Is it worth it/</text><text x="227" y="92">will people pay</text>
    </g>
  </svg>
  <span class="page">8</span>
</section>

<section class="slide">
  <h2 class="title" style="top:9px">What to ask?<br><span class="hl">Important Questions</span></h2>
  <div class="band">
    <div class="good">
      <p class="tag">Good <svg viewBox="0 0 12 12"><path d="M1 5h2v6H1zM4 5l3-4c1 0 1.5.6 1.2 2L8 5h2.6c.6 0 1 .5.8 1.1l-1 4.2c-.1.4-.5.7-.9.7H4z" fill="none" stroke="#222" stroke-width=".6"/></svg></p>
      <ul>
        <li>Imagine your company failed. Why did it fail? → Questions</li>
        <li>Imagine your company is huge success why? → Questions</li>
        <li>Ask those questions</li>
      </ul>
      <p style="font-weight:500;margin-top:2px">" you should be terrified of at least one of the questions you're asking in every conversation"</p>
    </div>
    <div class="bad">
      <p class="tag">Bad <svg viewBox="0 0 12 12" style="transform:rotate(180deg)"><path d="M1 5h2v6H1zM4 5l3-4c1 0 1.5.6 1.2 2L8 5h2.6c.6 0 1 .5.8 1.1l-1 4.2c-.1.4-.5.7-.9.7H4z" fill="none" stroke="#fff" stroke-width=".6"/></svg></p>
      <ul>
        <li>Deep inside, you are afraid your idea might be bad</li>
        <li>So you ask bogus questions</li>
      </ul>
    </div>
  </div>
  <span class="page">9</span>
</section>

<section class="slide">
  <h2 class="title" style="top:16px">!Mistakes to <span class="hl">Avoid</span></h2>
  <div class="band">
    <div class="photo" style="position:relative;width:96px;flex:none" role="img" aria-label="Photo of a woman with a headset making an OK gesture"></div>
    <div class="good" style="padding:18px 6px;font-size:5.4px;line-height:1.25">
      <p style="font-size:7px;margin-bottom:5px">STOP PITCHING YOUR PRODUCT</p>
      <p style="margin:0 0 5px 4px">"Let me show you our product.."</p>
      <p style="margin-bottom:4px">You are stop learning once you get into pitch mode and failed the mom's test.</p>
      <p style="font-weight:500">There is a time for it, but not when you are doing discovery customer calls</p>
    </div>
  </div>
  <span class="page">10</span>
</section>

<section class="slide">
  <h2 class="title" style="top:16px">What to ask? Get into <span class="hl">Specifics</span></h2>
  <div class="band">
    <div class="good" style="font-size:4px;padding:4px 8px">
      <p class="tag">Good <svg viewBox="0 0 12 12"><path d="M1 5h2v6H1zM4 5l3-4c1 0 1.5.6 1.2 2L8 5h2.6c.6 0 1 .5.8 1.1l-1 4.2c-.1.4-.5.7-.9.7H4z" fill="none" stroke="#222" stroke-width=".6"/></svg></p>
      <ul style="line-height:1.1">
        <li>Their life</li>
        <li>Specifics in the past</li>
        <li class="sub">How do you solve x now?</li><li class="sub">Why do you bother?</li><li class="sub">What are the implications</li>
        <li class="sub">Talk to me through the last time that happened.</li><li class="sub">Talk me through your workflow.</li>
        <li class="sub">What else have you tried?</li><li class="sub">Where do your funds come from?</li>
        <li>Who else should i talk to? → expand the target group</li>
        <li>Is there anything else I should have asked? → expand knowledge</li>
      </ul>
    </div>
    <div class="bad" style="font-size:5px">
      <p class="tag">Bad <svg viewBox="0 0 12 12" style="transform:rotate(180deg)"><path d="M1 5h2v6H1zM4 5l3-4c1 0 1.5.6 1.2 2L8 5h2.6c.6 0 1 .5.8 1.1l-1 4.2c-.1.4-.5.7-.9.7H4z" fill="none" stroke="#fff" stroke-width=".6"/></svg></p>
      <ul style="line-height:1.55">
        <li>Your idea</li><li>Generics, Opinions</li><li class="sub">Would you...</li>
        <li>Bad Data</li><li>Generics: "I always/never.."</li><li>Future : "I would/ will.."</li><li>Hypothetical:" I might could.."</li>
      </ul>
    </div>
  </div>
  <span class="page">11</span>
</section>

<section class="slide">
  <h2 class="title" style="top:16px">!Mistakes to <span class="hl">Avoid</span></h2>
  <div class="band">
    <div class="photo" style="position:relative;width:96px;flex:none;background:linear-gradient(135deg,#d6d6d6,#7d7d7d)" role="img" aria-label="Torn paper with a handwritten compliment"></div>
    <div class="good" style="padding:12px 6px;font-size:5.2px;line-height:1.3">
      <p style="margin-bottom:3px">EMPTY COMPLIMENTS</p>
      <p style="font-weight:500;margin-bottom:3px">Don't get flattered, it won't help your startup</p>
      <p style="margin-bottom:3px">Those are warning signal during a conversation. Direct the conversation away from you and back to the customer</p>
      <p>" I love this!",</p><p>" You are such a young bright student",</p><p>" this is a really good idea"</p>
    </div>
  </div>
  <span class="page">12</span>
</section>

<section class="slide">
  <h2 class="title" style="top:11px">!Things to <span class="hl">Get Excited</span> about</h2>
  <div class="band">
    <div class="photo" style="position:relative;width:96px;flex:none" role="img" aria-label="Photo of an excited young woman cheering"></div>
    <div class="good" style="padding:24px 6px;font-size:5.4px;line-height:1.3">
      <p style="margin-bottom:3px">Watch for EMOTIONAL REACTION</p>
      <p style="font-weight:500;margin-bottom:4px">"I see this frustrate you, tell me more? Yes i see.. what else? "</p>
      <p style="margin-bottom:4px">When someone get excited or share something that frustrate them -</p>
      <p>DIG in something is there.</p>
    </div>
  </div>
  <span class="page">13</span>
</section>

<section class="slide">
  <h2 class="title" style="top:9px">How to frame the conversation?<br><span class="hl">Casual</span></h2>
  <div class="band">
    <div class="good" style="font-size:5px">
      <p class="tag">Good <svg viewBox="0 0 12 12"><path d="M1 5h2v6H1zM4 5l3-4c1 0 1.5.6 1.2 2L8 5h2.6c.6 0 1 .5.8 1.1l-1 4.2c-.1.4-.5.7-.9.7H4z" fill="none" stroke="#222" stroke-width=".6"/></svg></p>
      <ul style="line-height:1.15">
        <li>Keep it casual</li>
        <li>Ideal: one one-meeting about the 3 best questions</li>
        <li class="sub" style="font-size:4.4px">Instead of asking: Do you have a time for a meeting with me? Ask simply your 3 questions, casually during a conversation. Pick one and add it in your email outreach.</li>
        <li>Takes maybe 5-15 mins</li>
      </ul>
    </div>
    <div class="bad" style="font-size:5px">
      <p class="tag">Bad <svg viewBox="0 0 12 12" style="transform:rotate(180deg)"><path d="M1 5h2v6H1zM4 5l3-4c1 0 1.5.6 1.2 2L8 5h2.6c.6 0 1 .5.8 1.1l-1 4.2c-.1.4-.5.7-.9.7H4z" fill="none" stroke="#fff" stroke-width=".6"/></svg></p>
      <ul style="line-height:1.3">
        <li>Customer development advises to have 3 meetings:</li>
        <li class="sub">the first about the customer and their problem</li>
        <li class="sub">the second about your solution</li>
        <li class="sub">the third to sell a product</li>
        <li>That takes a lot of time</li>
      </ul>
    </div>
  </div>
  <span class="page">14</span>
</section>

<section class="slide">
  <h2 class="title" style="top:11px">Commitments</h2>
  <div style="position:absolute;left:0;top:38px;width:256px;height:96px;background:var(--steel)"></div>
  <div style="position:absolute;left:16px;top:35px;display:flex;gap:8px">
    <div style="width:74px;height:96px;background:var(--steel);border:1.5px solid #999;border-radius:6px;padding:22px 3px 0;color:#fff;font-size:4.5px;line-height:1.2">
      <p style="font-size:6px;margin-bottom:3px">Time commitment</p>
      <ul><li>Clear next meeting with known goals</li><li>Sitting down to give feedback on wireframes</li><li>Using a trial themselves for a non-trivial period</li></ul>
    </div>
    <div style="width:74px;height:96px;background:var(--accent);border:1.5px solid #aaa;border-radius:6px;padding:20px 3px 0;color:#fff;font-size:4.5px;line-height:1.2">
      <p style="font-size:6px;margin-bottom:3px">Reputation Risk<br>(Social currency)</p>
      <ul><li>Intro to peers or team</li><li>Intro to a decision maker (Boss, Spouse, Lawyer)</li><li>Giving a public testimonial or case study</li></ul>
    </div>
    <div style="width:74px;height:96px;background:var(--mid);border:1.5px solid #bbb;border-radius:6px;padding:22px 3px 0;color:#fff;font-size:4.5px;line-height:1.2">
      <p style="font-size:6px;margin-bottom:3px">Money</p>
      <ul><li>Letter of intent ( non -legal but gentle agreement to purchase once ready)</li><li>Pre-order</li><li>Deposit</li></ul>
    </div>
  </div>
  <svg viewBox="0 0 12 12" style="position:absolute;left:77px;top:38px;width:10px;height:10px"><circle cx="6" cy="6" r="5" fill="none" stroke="#222" stroke-width=".8"/><path d="M6 3v3h2" fill="none" stroke="#222" stroke-width=".8"/></svg>
  <span class="page">15</span>
</section>

<section class="slide">
  <div class="photo dark" style="inset:0" role="img" aria-label="Black and white photo of two men talking at a table"></div>
  <div style="position:absolute;left:14px;top:15px;width:121px;height:122px;border:0.8px solid var(--accent)"></div>
  <p style="position:absolute;left:0;right:0;top:65px;text-align:center;color:#fff;font-size:9px;font-weight:300;line-height:1">How to find<br><b style="font-size:18px;font-weight:600">Customers</b></p>
</section>

<section class="slide">
  <h2 class="title" style="top:15px">Defining Research Audience</h2>
  <div style="position:absolute;left:22px;top:44px;width:69px;height:27px;background:var(--mid);border-radius:3px;color:#fff;font-size:3.8px;text-align:right;padding:5px 4px;line-height:1.2"><b>Proxies:</b> people who can speak on how the ideal audience thinks</div>
  <div style="position:absolute;left:22px;top:82px;width:69px;height:31px;background:var(--dark);border-radius:3px;color:#fff;font-size:4px;text-align:right;padding:13px 4px">Describe who they are</div>
  <div style="position:absolute;left:188px;top:44px;width:69px;height:30px;background:#b8b8b8;border-radius:3px;color:#fff;font-size:3.8px;padding:12px 4px">Identify the signal/ attributes</div>
  <div style="position:absolute;left:188px;top:82px;width:69px;height:31px;background:var(--mid);border-radius:3px;color:#fff;font-size:3.6px;padding:5px 4px;line-height:1.2"><b>Analogs:</b> people who look different from ideal audience but could provide similar insights</div>
  <svg viewBox="0 0 270 152" style="position:absolute;inset:0" font-family="Outfit,sans-serif">
    <circle cx="140" cy="80" r="38" fill="none" stroke="var(--accent)" stroke-width=".7" stroke-dasharray="2 1.5"/>
    <circle cx="140" cy="80" r="30" fill="#d9d9d9"/>
    <path d="M140 50a30 30 0 0 1 0 60z" fill="var(--mid)"/>
    <circle cx="140" cy="80" r="20" fill="#e6e6e6"/>
    <text x="140" y="79" font-size="4.5" text-anchor="middle">Ideal</text><text x="140" y="84" font-size="4.5" text-anchor="middle">Audience</text>
    <g fill="#e5e5e5" stroke="#aaa" stroke-width=".5"><circle cx="108" cy="56" r="7"/><circle cx="172" cy="56" r="7"/><circle cx="108" cy="104" r="7"/><circle cx="172" cy="104" r="7"/></g>
    <rect x="128" y="114" width="24" height="10" rx="2" fill="var(--accent)"/>
    <text x="140" y="118.5" font-size="3.2" fill="#fff" text-anchor="middle">Accessible</text><text x="140" y="122" font-size="3.2" fill="#fff" text-anchor="middle">Audience</text>
  </svg>
  <span class="page">17</span>
</section>

<section class="slide">
  <p class="title step" style="top:8px">STEP 1</p>
  <h2 class="title" style="top:19px;font-size:10px">Identify customer segment &amp; attributes</h2>
  <p style="position:absolute;left:0;right:0;top:39px;text-align:center;font-size:5px">How do your customers look like?</p>
  <div style="position:absolute;left:14px;top:50px;width:242px;display:flex;font-size:5.8px;color:#fff;text-align:center">
    <div style="flex:1;background:var(--mid);padding:3px">B2B ( Business to Business)</div>
    <div style="flex:1;background:var(--accent);padding:3px">B2C ( business to consumers)</div>
  </div>
  <div style="position:absolute;left:14px;top:62px;width:242px;height:26px;background:#e3e3e3;display:flex;font-size:5px;line-height:1.3;padding:3px 0">
    <ul style="flex:1;padding-left:18px"><li>Company size</li><li>Industry</li><li>Role/ title</li></ul>
    <ul style="flex:1;padding-left:6px"><li>Demographics: age, gender, profession, income layer, interests, single/family, etc.)</li></ul>
  </div>
  <div style="position:absolute;left:16px;right:16px;top:99px;text-align:center;font-size:5px;line-height:1.25">
    <p style="margin-bottom:3px">Pick 2-3 different customer segments and initiate conversations</p>
    <p style="margin-bottom:2px">You will start hearing the same thing after 4-5 interviews, if you are hearing new things after 10+ interview your segment is too broad.</p>
    <p style="font-weight:500">If you can't find them, you'll never advertise or sell to them</p>
  </div>
  <span class="page">18</span>
</section>

<section class="slide">
  <p class="title step" style="top:8px">STEP 1</p>
  <h2 class="title" style="top:19px;font-size:10px">Finding Initial Conversation</h2>
  <div class="photo" style="left:0;top:40px;width:111px;height:92px;background:linear-gradient(135deg,#d5d5d5,#6b6b6b)" role="img" aria-label="Black and white photo of a busy office"></div>
  <ul style="position:absolute;left:115px;top:40px;width:140px;font-size:4.2px;line-height:1.28">
    <li>Cold Calls/emails - 2 out of 100 will talk to you</li>
    <li>Serendipity - there are often cool people already around you</li>
    <li>Find a good excuse:</li>
    <li class="sub" style="font-size:3.5px">I do my PhD on... Can i ask you some questions</li>
    <li class="sub" style="font-size:3.5px">I'm a student in ..</li>
    <li>Immerse yourself in where they are</li>
    <li>Social media platforms</li>
    <li>Organize meetups :)</li>
    <li>Landing pages</li>
    <li>Industry blogging</li>
    <li>Get clever :)</li>
    <li>"The goal of cold conversation is to stop having them"</li>
  </ul>
  <span class="page">19</span>
</section>

<section class="slide">
  <p class="title step" style="top:8px">STEP 2</p>
  <h2 class="title" style="top:19px;font-size:10px">Creating warm intros Initial Conversation</h2>
  <div class="photo dark" style="left:0;top:40px;width:111px;height:92px" role="img" aria-label="Black and white photo of hands over a table in a meeting"></div>
  <ul style="position:absolute;left:115px;top:40px;width:146px;font-size:4.3px;line-height:1.28">
    <li>7 degree of separations - "you can find anything you need if you ask for it a couple of times"</li>
    <li>Industry advisors</li>
    <li>Colleges ( Hint, hint)</li>
    <li>Professors</li>
    <li>Try to avoid a "real meeting", if possible ( keep it casual)</li>
    <li class="sub" style="font-size:3.8px">Vision : what we aim for, broadly</li>
    <li class="sub" style="font-size:3.8px">Framing : why we meet you, what we expect</li>
    <li class="sub" style="font-size:3.8px">Weakness : why we need you</li>
    <li class="sub" style="font-size:3.8px">Pedestal: a compliment</li>
    <li class="sub" style="font-size:3.8px">Ask try to get more commitments</li>
  </ul>
  <span class="page">20</span>
</section>

<section class="slide">
  <h2 class="title" style="top:11px">Customer conversation &amp; your team</h2>
  <div class="photo dark" style="left:0;top:38px;width:270px;height:96px" role="img" aria-label="Dark photo of a team at work"></div>
  <div style="position:absolute;left:13px;top:35px;display:flex;gap:8px;font-size:3.6px;line-height:1.2;color:#fff">
    <div style="width:74px;height:99px;background:var(--steel);border:1.5px solid #999;border-radius:6px;padding:10px 3px 0">
      <p style="font-size:5.2px;margin-bottom:3px">Prepping (Together with your team)</p>
      <ul><li>Choose the right 3 scary questions ( if the answer is on search, search it)</li><li>1-2 persons : 1) talking 2) note-taking &amp; fixing conversations</li><li>Due diligence on social profiles about your conversation partner</li><li>Write down your assumptions about a person to validate them later</li><li>Decide on what commitment you want</li></ul>
    </div>
    <div style="width:74px;height:99px;background:var(--accent);border:1.5px solid #aaa;border-radius:6px;padding:10px 3px 0">
      <p style="font-size:5.2px;margin-bottom:3px">Doing</p>
      <p style="font-size:4px">Who should who up</p>
      <ul><li>Those who make decisions ( at least to some meetings)</li></ul>
      <p style="font-size:4px">How to write it down:</p>
      <ul><li>Note Emotions, problems, goals, workarounds, obstacles, ideas/feature request, budget/buying process, follow up -task, reference person/companies</li><li>Maybe use 1 card for one information item</li></ul>
    </div>
    <div style="width:74px;height:99px;background:var(--mid);border:1.5px solid #bbb;border-radius:6px;padding:10px 3px 0">
      <p style="font-size:5.2px;margin-bottom:3px">Reviewing</p>
      <ul><li>Review notes, update written assumptions, update 3 questions</li><li>How can you improve to learn better next time</li></ul>
    </div>
  </div>
</section>

<section class="slide">
  <h2 class="title" style="top:11px">Homework</h2>
  <div class="photo dark" style="left:0;top:42px;width:270px;height:86px" role="img" aria-label="Dark photo of an open book"></div>
  <div style="position:absolute;left:12px;top:65px;width:246px;display:flex;color:#fff;text-align:center">
    <div style="flex:1;border-right:.5px solid #888"><p style="font-size:14px;font-weight:600">1</p><p style="font-size:3.9px">Pick 3 scary questions</p></div>
    <div style="flex:1;border-right:.5px solid #888"><p style="font-size:14px;font-weight:600">2</p><p style="font-size:3.9px">Identify 3 learning goals and 2-3 questions for each</p></div>
    <div style="flex:1;border-right:.5px solid #888"><p style="font-size:14px;font-weight:600">3</p><p style="font-size:3.9px">Identify 2 audience segments and its attributes</p></div>
    <div style="flex:1;border-right:.5px solid #888"><p style="font-size:14px;font-weight:600">4</p><p style="font-size:3.9px">Find &amp; outreach &amp; Do your first 3 conversations ( 10-15 mins interviews)</p></div>
    <div style="flex:1"><p style="font-size:14px;font-weight:600">5</p><p style="font-size:3.9px">Debrief with your team on the learning and set new learning goals</p></div>
  </div>
</section>

<section class="slide">
  <p style="position:absolute;left:0;right:0;top:26px;text-align:center;font-size:10px;font-weight:300;line-height:1.05">Thank you for listening...<br><b style="font-size:17px;font-weight:600">Any Questions?</b></p>
  <div style="position:absolute;left:202px;top:48px;width:32px;height:94px;border:.7px solid var(--accent);border-left:none"></div>
  <div style="position:absolute;left:110px;top:126px;width:124px;height:16px;border:.7px solid var(--accent);border-top:none;border-right:none"></div>
  <div class="photo" style="left:0;top:62px;width:270px;height:70px;background:linear-gradient(90deg,#5a5a5a,#8c86f0 55%,#7d76f3)" role="img" aria-label="Purple tinted photo of a handshake"></div>
  <span class="page">23</span>
</section>

<section class="slide">
  <div class="photo" style="inset:0;background:linear-gradient(135deg,#f2f2f2,#a9a9a9 60%,#555)" role="img" aria-label="Black and white photo of hands typing on a laptop"></div>
  <div style="position:absolute;left:32px;top:41px;width:82px;height:64px;background:rgba(107,99,246,.55)"></div>
  <div style="position:absolute;left:34px;top:54px;color:#fff;line-height:1.1">
    <p style="font-size:11px;font-weight:600">Contact</p>
    <p style="font-size:5px">Mara Ostrin</p>
    <p style="font-size:5px">Co-Founder Northbank Learning</p>
    <p style="font-size:5px">mara.ostrin@mail.example</p>
  </div>
  <div style="position:absolute;left:125px;top:60px;display:flex;flex-direction:column;gap:3px">
    <span style="width:8px;height:8px;border:.6px solid #fff;border-radius:50%"></span>
    <span style="width:8px;height:8px;border:.6px solid #fff;border-radius:50%"></span>
    <span style="width:8px;height:8px;border:.6px solid #fff;border-radius:50%"></span>
  </div>
</section>

</main>
</body>
</html>
```